Pebble nook day nursery qrv limited

we would like create a website that can be updated by us easily as we have regular changes to what we provide and need. we would like something that is classy but also appealing from a child's aspect. we would be looking to add our own logo and our edvarin logo both attached, if you guys can create it and we will work with the preferred choice to add all the text.
We would like the links to kin pathways, edvarin report and our chatterloom feed on the front page

we are looking for a website for our childcare business we have 2 nurseries that we would like one website.
showing our opening hours, price list, policies etc as well as photos, description of our day, staff photos and their training accreditation's.

Target Market(s)

Families

Industry/Entity Type

Childcare

Number of Pages Required

5+ page

Font styles to use
Serif

Colors

Designer to choose colors to be used in the design.

Requirements
Must have
• links to social media and other websites, photographs, links to download registration forms etc, parents able to leave reviews. wayrund plots link, job opportunities
Nice to have
• facilities to take payments

```html
<!DOCTYPE html>
<html lang="en">
<head>
<meta charset="utf-8">
<title>Pebble Nook Day Nursery QRV Limited</title>
<link href="https://fonts.googleapis.com/css2?family=Exo+2:wght@500;600;700&family=Open+Sans:ital,wght@0,400;0,600;0,700;1,600&display=swap" rel="stylesheet">
<style>
:root{
  --navy:#1b2b72;
  --navy-deep:#0f2766;
  --magenta:#d2246f;
  --green:#5aa832;
  --orange:#e5822b;
  --ink:#333;
  --muted:#555;
  --dark-btn:#333;
  --pale:#ececec;
  --white:#fff;
}
*{margin:0;padding:0;box-sizing:border-box}
html,body{width:1200px;height:3098px;overflow:hidden;background:var(--white)}
body{font-family:"Open Sans",Arial,sans-serif;color:var(--ink);position:relative}
.abs{position:absolute}
section,header,footer{position:absolute;left:0;width:1200px}
h2{font-family:"Exo 2",Arial,sans-serif;font-weight:700;font-size:31px;color:var(--navy);text-align:center;position:absolute;left:0;width:1200px}
.rule{position:absolute;left:575px;width:50px;height:3px;background:var(--magenta)}
.center{text-align:center;left:0;width:1200px}

/* header */
.site-header{top:0;height:138px;background:var(--white)}
.brand{left:160px;top:34px;display:flex;align-items:center;gap:12px}
.brand-mark{width:34px;height:34px;background:var(--green)}
.brand-name{font-family:"Exo 2",sans-serif;font-weight:700;font-size:26px;color:var(--navy);line-height:1.05;width:260px}
.top-btn{top:20px;height:26px;font-size:12px;font-weight:600;color:var(--white);display:flex;align-items:center;justify-content:center}
.btn-location{left:632px;width:112px;background:#555}
.btn-enroll{left:760px;width:104px;background:var(--green)}
.phone{left:878px;top:16px;display:flex;align-items:center;gap:8px;font-family:"Exo 2",sans-serif;font-size:21px;font-weight:600;color:var(--navy)}
.main-nav{top:104px;left:543px;display:flex;font-size:13px;font-weight:600;color:var(--navy)}
.main-nav span{padding:0 12px;border-left:1px solid #bbb;line-height:14px}
.main-nav span:first-child{border:0;padding-left:0;color:var(--magenta)}

/* hero */
.hero{top:138px;height:482px;background:linear-gradient(120deg,#c9823a 0%,#e2a35a 30%,#d9c4a0 55%,#9a6f4a 80%,#6d8a5a 100%)}
.slide-arrow{top:230px;width:26px;height:26px;background:rgba(0,0,0,.6);display:flex;align-items:center;justify-content:center}
.hero-caption{top:436px;left:0;width:1200px;height:46px;background:rgba(20,20,20,.7);color:var(--white);font-size:24px;display:flex;align-items:center;justify-content:center}

/* welcome */
.welcome{top:620px;height:295px}
.welcome h2{top:34px}
.welcome .rule{top:82px}
.welcome .lead{top:96px;font-size:14px;color:var(--muted)}
.welcome .body{top:128px;left:171px;width:858px;font-size:11.5px;line-height:20px;color:var(--muted);text-align:center}
.btn-read{top:214px;left:535px;width:130px;height:34px;background:var(--dark-btn);color:var(--white);font-size:13px;display:flex;align-items:center;justify-content:center}

/* programs */
.programs{top:915px;height:460px;background:linear-gradient(180deg,#4b4b4b,#5c4d4a 50%,#3f3a3a)}
.programs h2{top:30px;color:var(--white)}
.programs .rule{top:78px}
.program{top:138px;width:240px;text-align:center}
.program .photo{width:178px;height:178px;border-radius:50%;margin:0 auto;border:8px solid rgba(200,200,200,.6);background:linear-gradient(135deg,#d9b99b,#b98a6e)}
.program h3{font-family:"Exo 2",sans-serif;font-size:19px;font-weight:600;margin-top:12px}
.program .age{color:var(--white);font-weight:700;font-size:12px;margin-top:6px}
.program p{color:var(--white);font-size:12px;line-height:20px;margin-top:4px}
.pink{color:var(--magenta)}.grn{color:var(--green)}

/* why */
.why{top:1375px;height:401px}
.why h2{top:40px}
.why .rule{top:88px}
.why .intro{top:100px;left:190px;width:820px;font-size:12px;font-weight:600;line-height:21px;text-align:center;color:var(--ink)}
.feature{top:159px;width:240px;text-align:center}
.feature .icon{width:104px;height:104px;border-radius:50%;border:2px solid #777;margin:0 auto;display:flex;align-items:center;justify-content:center}
.feature h3{font-size:13px;font-weight:700;margin-top:18px;color:var(--ink)}
.feature p{font-size:11.5px;line-height:21px;color:var(--muted);margin-top:12px}
.feature .more{font-size:10px;color:var(--muted)}

/* reviews */
.reviews{top:1776px;height:384px;background:var(--pale)}
.reviews h2{top:38px}
.reviews .rule{top:86px}
.review-text{top:106px;left:173px;width:854px;font-size:11.5px;font-style:italic;line-height:22px;color:var(--muted);text-align:center}
.avatar{top:201px;left:562px;width:76px;height:76px;border-radius:50%;border:4px solid var(--orange);background:linear-gradient(180deg,#b9c2cf,#6e7b8f)}
.reviewer{top:286px;font-family:Georgia,serif;font-size:15px;font-weight:700;color:var(--orange);font-style:italic}
.stars{top:310px;font-size:14px;color:#f0b323;letter-spacing:2px}
.dots{top:338px;left:583px;display:flex;gap:6px}
.dots i{width:12px;height:12px;border-radius:50%;border:1px solid #999;display:block}
.dots i:last-child{background:#999}

/* gallery */
.gallery{top:2160px;height:258px}
.gallery h2{top:36px}
.gallery .rule{top:84px}
.thumb{top:113px;width:166px;height:106px;border:4px solid var(--white);box-shadow:0 1px 5px rgba(0,0,0,.35);background:linear-gradient(135deg,#e8c48c,#d47a5a 60%,#7aa0c8)}
.thumb.hover{background:linear-gradient(135deg,#5c5c5c,#3e3e3e);color:var(--white);font-size:12px;font-weight:600;display:flex;align-items:center;justify-content:center;text-align:center;padding:0 20px}
.g-arrow{top:150px;font-size:26px;color:#222;font-weight:700}

/* contact */
.contact{top:2418px;height:597px;background:linear-gradient(180deg,#4a4645,#6a5a52 45%,#5a5048 80%,#3c3835)}
.contact h2{top:38px;color:var(--white)}
.contact .rule{top:86px;left:560px;width:80px;background:var(--white)}
.info{top:124px;width:240px;text-align:center;color:var(--white)}
.info h4{font-size:14px;font-weight:600;margin-top:10px}
.info p{font-size:12px;font-weight:600;line-height:18px;margin-top:4px}
.form-panel{top:242px;left:180px;width:842px;height:297px;background:rgba(120,120,120,.6)}
.form-panel .t1{top:22px;font-size:17px;color:var(--white);font-weight:600;left:0;width:842px;text-align:center}
.form-panel .t2{top:48px;font-size:20px;color:var(--white);font-weight:600;left:0;width:842px;text-align:center}
.field{background:rgba(255,255,255,.55);font-size:11px;color:#444;padding:8px 10px}
.submit{background:var(--green);color:var(--navy-deep);font-weight:700;font-size:14px;display:flex;align-items:center;justify-content:center}
.badge{left:878px;width:117px;background:var(--navy);border-radius:4px}

/* footer */
.site-footer{top:3015px;height:83px;background:var(--navy-deep);color:var(--white)}
.foot-nav{top:18px;left:165px;display:flex;font-size:12px;font-weight:600}
.foot-nav span{padding:0 13px;border-left:1px solid #ccc;line-height:13px}
.foot-nav span:first-child{border:0;padding-left:0}
.copy{top:57px;left:165px;font-size:11px}
.fees{top:10px;left:885px;display:flex;align-items:center;gap:8px;font-size:12px}
.follow{top:48px;left:843px;display:flex;align-items:center;gap:6px;font-size:12px}
.follow i{width:28px;height:28px;border-radius:50%;border:2px solid var(--white);display:block}
</style>
</head>
<body>

<header class="site-header">
  <div class="abs brand"><span class="brand-mark"></span><span class="brand-name">Pebble Nook Day Nursery QRV</span></div>
  <div class="abs top-btn btn-location">Our Location »</div>
  <div class="abs top-btn btn-enroll">Enroll Now »</div>
  <div class="abs phone">
    <svg width="24" height="24" viewBox="0 0 24 24"><circle cx="12" cy="12" r="11" fill="none" stroke="#d2246f" stroke-width="1.5"/><path d="M8 6l2 0 1 3-1.5 1a7 7 0 0 0 4 4l1-1.5 3 1v2c-5 1-10-4-9.5-9.5z" fill="#d2246f"/></svg>
    555-014-2290
  </div>
  <nav class="abs main-nav"><span>Home</span><span>About Us</span><span>Our Services</span><span>Price</span><span>Gallery</span><span>Contact Us</span></nav>
</header>

<section class="hero" role="img" aria-label="Photograph of a bright nursery playroom with toys, play tent and reading corner">
  <div class="abs slide-arrow" style="left:0"><svg width="10" height="12"><path d="M8 1L2 6l6 5" fill="none" stroke="#fff" stroke-width="2"/></svg></div>
  <div class="abs slide-arrow" style="right:0"><svg width="10" height="12"><path d="M2 1l6 5-6 5" fill="none" stroke="#fff" stroke-width="2"/></svg></div>
  <div class="abs hero-caption">Day Nurseries Providing Full Day Care For Children In The UK</div>
</section>

<section class="welcome">
  <h2>Welcome to Pebble Nook Day Nursery</h2>
  <div class="rule"></div>
  <p class="abs center lead">Duis autem vel eum iriure dolor in hendrerit in vulputate velit esse molestie consequat, vel illum dolore.</p>
  <p class="abs body">Lorem ipsum dolor sit amet, consectetuer adipiscing elit, sed diam nonummy nibh euismod tincidunt ut laoreet dolore magna aliquam erat volutpat. Ut wisi enim ad minim veniam, quis nostrud exerci tation ullamcorper suscipit lobortis nisl ut aliquip ex ea commodo consequat. Duis autem vel eum iriure dolor in hendrerit in vulputate velit esse molestie consequat, vel illum dolore eu feugiat nulla facilisis at vero eros et accumsan et iusto odio dignissim qui blandit praesent luptatum zzril delenit augue duis dolore te feugait nulla facilisi.</p>
  <div class="abs btn-read">Read More</div>
</section>

<section class="programs" role="img" aria-label="Background photograph of young children playing together">
  <h2>Our Programs</h2>
  <div class="rule"></div>
  <div class="abs program" style="left:144px"><div class="photo" role="img" aria-label="Photo of infants"></div><h3 class="pink">Infant</h3><p class="age">Age 6 Weeks - 18 Months</p><p>Lorem ipsum dolor sit amet, tuer<br>adipiscing elit ed diam.</p></div>
  <div class="abs program" style="left:371px"><div class="photo" role="img" aria-label="Photo of a toddler playing"></div><h3 class="grn">Toddler</h3><p class="age">Age 18 -36 Months</p><p>Lorem ipsum dolor sit amet, tuer<br>adipiscing elit ed diam.</p></div>
  <div class="abs program" style="left:597px"><div class="photo" role="img" aria-label="Photo of a pre-school child"></div><h3 class="pink">Pre-School</h3><p class="age">Age 3-5 Years</p><p>Lorem ipsum dolor sit amet, tuer<br>adipiscing elit ed diam.</p></div>
  <div class="abs program" style="left:824px"><div class="photo" role="img" aria-label="Photo of a kindergarten classroom"></div><h3 class="grn">Kindergarten</h3><p class="age">Kindergarten-12 years</p><p>Lorem ipsum dolor sit amet, tuer<br>adipiscing elit ed diam.</p></div>
</section>

<section class="why">
  <h2>Why Choose Us</h2>
  <div class="rule"></div>
  <p class="abs intro">Lorem ipsum dolor sit amet, consectetuer adipiscing elit, sed diam nonummy nibh euismod tincidunt ut laoreet dolore magna aliquam erat volutpat. Ut wisi enim ad minim veniam, quis nostrud exerci tation ullamcorper suscipi.</p>
  <div class="abs feature" style="left:136px"><div class="icon"><svg width="44" height="44" viewBox="0 0 44 44"><circle cx="15" cy="14" r="9" fill="none" stroke="#222" stroke-width="3"/><path d="M21 21l14 14" stroke="#222" stroke-width="4"/></svg></div><h3>Fun Leaning</h3><p>Lorem ipsum dolor sit amet sit amet<br>ipsum dolor sit amet, dolor sit amet...</p><span class="more">[+]</span></div>
  <div class="abs feature" style="left:363px"><div class="icon"><svg width="44" height="44" viewBox="0 0 44 44"><rect x="8" y="6" width="24" height="32" fill="none" stroke="#222" stroke-width="3"/><path d="M13 14h14M13 20h14M13 26h8" stroke="#222" stroke-width="2"/><circle cx="32" cy="32" r="8" fill="#222"/><path d="M28 32l3 3 5-6" fill="none" stroke="#fff" stroke-width="2"/></svg></div><h3>Easy Academics</h3><p>Lorem ipsum dolor sit amet sit amet<br>ipsum dolor sit amet, dolor sit amet...</p><span class="more">[+]</span></div>
  <div class="abs feature" style="left:594px"><div class="icon"><svg width="44" height="44" viewBox="0 0 44 44"><circle cx="22" cy="18" r="9" fill="none" stroke="#222" stroke-width="3"/><path d="M18 30h8M19 35h6" stroke="#222" stroke-width="3"/><path d="M22 3v4M8 18h-4M40 18h-4M11 7l3 3M33 7l-3 3" stroke="#222" stroke-width="2"/></svg></div><h3>Innovative Approach</h3><p>Lorem ipsum dolor sit amet sit amet<br>ipsum dolor sit amet, dolor sit amet...</p><span class="more">[+]</span></div>
  <div class="abs feature" style="left:826px"><div class="icon"><svg width="44" height="44" viewBox="0 0 44 44"><circle cx="10" cy="12" r="4" fill="#222"/><path d="M6 18h8v22H6z" fill="#222"/><rect x="18" y="6" width="22" height="16" fill="none" stroke="#222" stroke-width="3"/><path d="M14 20l8-6" stroke="#222" stroke-width="2"/></svg></div><h3>Qualified Staff</h3><p>Lorem ipsum dolor sit amet sit amet<br>ipsum dolor sit amet, dolor sit amet...</p><span class="more">[+]</span></div>
</section>

<section class="reviews">
  <h2>Parent Reviews</h2>
  <div class="rule"></div>
  <p class="abs review-text">“ Lorem ipsum sit amet co adipiscitsed udml eisll mol monk dtepor incidunt ut la dolore ma aliquamm kn nibhmi enim nim veni exercitation ullamco ips sdttnol am conoplk adipiscig elitsedm do eiusmod te epo uom accuil dollarmjk oremque laantium. Accusant dolorempuen more consec moptnonumyr facilies Lorem ipsum sit amet co adipiscitsed udml eisll mol monk dtepor incidunt ut la dolore ma aliquamm kn nibhmi enim nim veni exercitation ullamco ips sdttnol am conoplk adipiscig elitsedm do eiusmod te epo uom accuil dollarmjk oremque laudantium. Accusant ”</p>
  <div class="abs avatar" role="img" aria-label="Portrait of the reviewing parent"></div>
  <p class="abs center reviewer">- Marek Olsten</p>
  <p class="abs center stars">★★★★☆</p>
  <div class="abs dots"><i></i><i></i></div>
</section>

<section class="gallery">
  <h2>Photo Gallery</h2>
  <div class="rule"></div>
  <span class="abs g-arrow" style="left:138px">‹</span>
  <div class="abs thumb" style="left:161px" role="img" aria-label="Photo of children at a craft table"></div>
  <div class="abs thumb hover" style="left:341px">Lorem Ipsum is the dummy text</div>
  <div class="abs thumb" style="left:520px" role="img" aria-label="Photo of children in a classroom"></div>
  <div class="abs thumb" style="left:702px" role="img" aria-label="Photo of children playing with blocks"></div>
  <div class="abs thumb" style="left:878px" role="img" aria-label="Photo of children painting"></div>
  <span class="abs g-arrow" style="left:1052px">›</span>
</section>

<section class="contact" role="img" aria-label="Background photograph of the nursery building and outdoor play area">
  <h2>Contact Us</h2>
  <div class="rule"></div>
  <div class="abs info" style="left:136px"><svg width="22" height="28" viewBox="0 0 22 28"><path d="M11 1a9 9 0 0 0-9 9c0 7 9 17 9 17s9-10 9-17a9 9 0 0 0-9-9z" fill="#fff"/><circle cx="11" cy="10" r="3.5" fill="#5a504a"/></svg><h4>Location</h4><p>Street Name, City Name<br>State Zipcode</p></div>
  <div class="abs info" style="left:359px"><svg width="24" height="28" viewBox="0 0 24 28"><rect x="1" y="7" width="22" height="15" fill="#fff"/><path d="M1 7l11 9 11-9" fill="none" stroke="#5a504a" stroke-width="2"/></svg><h4>Email</h4><p>inquiry@pebblenooknursery.com</p></div>
  <div class="abs info" style="left:557px"><svg width="24" height="28" viewBox="0 0 24 28"><path d="M5 3l5 0 2 6-3 2a12 12 0 0 0 6 7l2-3 6 2v5c-11 2-20-8-18-19z" fill="#fff"/></svg><h4>Call</h4><p>555-014-2290</p></div>
  <div class="abs info" style="left:782px"><svg width="24" height="28" viewBox="0 0 24 28"><circle cx="12" cy="14" r="10" fill="none" stroke="#fff" stroke-width="2.5"/><path d="M12 8v6l4 3" stroke="#fff" stroke-width="2.5" fill="none"/></svg><h4>Timing</h4><p>Mon. To Sat.: 10.00 a.m. to - 04.00 p.m.<br>Sunday : Close</p></div>

  <div class="abs form-panel">
    <p class="abs t1">Get In Touch</p>
    <p class="abs t2">Have Questions ?  Well be happy  To Answes!</p>
    <div class="abs field" style="left:57px;top:86px;width:283px;height:30px">Name</div>
    <div class="abs field" style="left:357px;top:86px;width:285px;height:30px">Email</div>
    <div class="abs field" style="left:57px;top:126px;width:283px;height:31px">Inquiry for class</div>
    <div class="abs field" style="left:357px;top:126px;width:285px;height:31px">Phone</div>
    <div class="abs field" style="left:57px;top:169px;width:585px;height:66px">Inquiry message</div>
    <div class="abs submit" style="left:57px;top:248px;width:585px;height:33px">SUBMIT</div>
  </div>
  <div class="abs badge" style="top:287px;height:114px" role="img" aria-label="Edvarin rating badge 2009-2010"></div>
  <div class="abs badge" style="top:415px;height:116px" role="img" aria-label="Edvarin rating badge 2012-2013"></div>
</section>

<footer class="site-footer">
  <nav class="abs foot-nav"><span>Home</span><span>About Us</span><span>Our Services</span><span>Price</span><span>Gallery</span><span>Contact Us</span></nav>
  <p class="abs copy">Copyright © 2017 Pebble Nook Day Nursery QRV Limited. All Rights Reserved.</p>
  <div class="abs fees"><svg width="22" height="18" viewBox="0 0 22 18"><rect x="1" y="3" width="18" height="12" fill="#fff"/><rect x="1" y="6" width="18" height="2" fill="#0f2766"/></svg>Pay Your Fees Here</div>
  <div class="abs follow">Follow Us <i aria-label="Chatterloom"></i><i></i><i></i><i></i></div>
</footer>

</body>
</html>
```